Enterprise image desing

The designs are for a fashion store for young men and women.
Updates

Los diseƱos parecen similares

Target Market(s)

Young

Font styles to use
Sans Serif

Colors
ec1f27
ffffff
1b1b1b

Requirements
Must have
• Use clean and modern sources
Nice to have
• n / a
Should not have
• n / a

```html
<!DOCTYPE html>
<html lang="es">
<head>
<meta charset="utf-8">
<title>Varento – Tarjeta de presentación</title>
<link href="https://fonts.googleapis.com/css2?family=Work+Sans:wght@400;500;700&display=swap" rel="stylesheet">
<style>
  :root {
    --backdrop: #dcdcdc;
    --card-black: #1b1b1b;
    --brand-red: #ec1f27;
    --emboss-grey: #333333;
    --ink-white: #ffffff;
    --ink-soft: #cfcfcf;
    --divider: #ec1f27;
  }
  * { box-sizing: border-box; margin: 0; padding: 0; }
  html, body { width: 1200px; height: 900px; overflow: hidden; }
  body {
    background: var(--backdrop);
    font-family: "Work Sans", Arial, sans-serif;
    display: flex;
    flex-direction: column;
    align-items: center;
    justify-content: center;
    gap: 50px;
  }
  .card {
    width: 640px;
    height: 366px;
    background: var(--card-black);
    position: relative;
  }
  .card-front {
    display: flex;
    align-items: center;
    justify-content: center;
  }
  .brand {
    display: flex;
    align-items: center;
    gap: 16px;
  }
  .brand-square {
    width: 50px;
    height: 50px;
    background: var(--brand-red);
  }
  .brand-name {
    font-weight: 700;
    font-size: 60px;
    letter-spacing: 2px;
    color: var(--ink-white);
  }
  .card-back {
    display: flex;
    align-items: center;
    padding: 0 36px 0 34px;
  }
  .card-back .brand { gap: 12px; width: 300px; }
  .card-back .brand-square { width: 34px; height: 34px; background: var(--emboss-grey); }
  .card-back .brand-name { font-size: 40px; letter-spacing: 1.5px; color: var(--emboss-grey); }
  .divider {
    width: 2px;
    height: 196px;
    background: var(--divider);
    margin-right: 28px;
    flex: none;
  }
  .contact { color: var(--ink-white); white-space: nowrap; }
  .contact-name { font-size: 19px; font-weight: 500; letter-spacing: 1px; }
  .contact-role { font-size: 15px; color: var(--brand-red); letter-spacing: 1px; margin-bottom: 12px; }
  .contact-address { font-size: 15px; color: var(--ink-soft); line-height: 1.3; letter-spacing: 0.6px; margin-bottom: 10px; }
  .contact-list { list-style: none; font-size: 17px; letter-spacing: 0.8px; }
  .contact-list li { display: flex; align-items: center; gap: 10px; line-height: 1.35; }
  .contact-list svg { width: 12px; height: 12px; flex: none; }
</style>
</head>
<body>
  <section class="card card-front">
    <div class="brand">
      <span class="brand-square"></span>
      <span class="brand-name">VARENTO</span>
    </div>
  </section>

  <section class="card card-back">
    <div class="brand">
      <span class="brand-square"></span>
      <span class="brand-name">VARENTO</span>
    </div>
    <span class="divider"></span>
    <div class="contact">
      <p class="contact-name">MARCO IBARRA LEÓN</p>
      <p class="contact-role">Gerente General</p>
      <p class="contact-address">Calle Olmedo y Sucre,<br>Ecuador, EC070105</p>
      <ul class="contact-list">
        <li>
          <svg viewBox="0 0 12 12" fill="var(--brand-red)"><path d="M2.5 1h2l1 3-1.3 1a6 6 0 0 0 2.8 2.8l1-1.3 3 1v2a1 1 0 0 1-1 1A9.5 9.5 0 0 1 1.5 2a1 1 0 0 1 1-1z"/></svg>
          +593 7 410-2286
        </li>
        <li>
          <svg viewBox="0 0 12 12" fill="none" stroke="var(--brand-red)" stroke-width="1.2"><rect x="3" y="0.8" width="6" height="10.4" rx="1"/><line x1="5" y1="9.4" x2="7" y2="9.4"/></svg>
          +593 98 615-3072
        </li>
        <li>
          <svg viewBox="0 0 12 12" fill="none" stroke="var(--brand-red)" stroke-width="1.2"><rect x="0.8" y="2.3" width="10.4" height="7.4"/><path d="M0.8 2.3 6 6.5l5.2-4.2"/></svg>
          mibarra@varento.com
        </li>
        <li>
          <svg viewBox="0 0 12 12" fill="none" stroke="var(--brand-red)" stroke-width="1.1"><circle cx="6" cy="6" r="5.2"/><ellipse cx="6" cy="6" rx="2.3" ry="5.2"/><line x1="0.8" y1="6" x2="11.2" y2="6"/></svg>
          www.varento.com
        </li>
      </ul>
    </div>
  </section>
</body>
</html>
```